brightquokka.net we need a webpage designed for our new product

We need a webpage designed for our new range of products from our new brand. We have had a logo designed on sketchhive (see attached) and we want to keep to this theme. Our first product is a range of affordable app controlled LED lightbulbs.

I have added some photos that we think is good inspirational material and would be good as a background to this website, but we want the site to look modern but not conventional. We would like something that makes our company look quirky not corporate.

Thats it

Target Market(s)

Our product is being stocked by big name online retailers in the UK, the page will get link through hits from our app. Our target market is gadget freaks of all ages.

Industry/Entity Type

It Company

Requirements
Must have
• We are going to need a help page, text to be uploaded next few days.

We need a contact page.

design my work on iOS and Android as most people will access page through their handset or tablet.
Should not have
• We do not want anything too corporate.

```html
<!DOCTYPE html>
<html lang="en">
<head>
<meta charset="utf-8">
<title>Bright Quokka — Home</title>
<link href="https://fonts.googleapis.com/css2?family=Roboto+Condensed:wght@300;400;700&family=Lato:wght@400;700&family=Open+Sans:wght@400;600&display=swap" rel="stylesheet">
<style>
:root{
  --green:#3fae49;
  --green-dark:#2e8f37;
  --nav:#4b4b4b;
  --nav-line:#5f5f5f;
  --ink:#333;
  --muted:#555;
  --panel:#e6e6e6;
  --footer:#e0e0e0;
  --bar:#4d4d4d;
  --white:#fff;
}
*{box-sizing:border-box;margin:0;padding:0}
html,body{width:763px;height:1200px;overflow:hidden;background:var(--white)}
body{position:relative;font-family:"Lato",sans-serif;color:var(--ink)}
.abs{position:absolute}

/* header */
.header-rule{left:0;top:96px;width:763px;height:3px;background:var(--green)}
.brand-box{left:30px;top:0;width:128px;height:172px;background:var(--white);border:2px solid var(--green);border-top:none;display:flex;align-items:flex-end;justify-content:center;padding-bottom:14px;z-index:3}
.brand-name{font-family:"Roboto Condensed",sans-serif;font-weight:700;font-size:10px;color:var(--green);letter-spacing:.3px}
.cart{left:418px;top:32px;width:140px;height:32px;background:#b9dcab;display:flex}
.cart-bag{width:35px;height:32px;background:#2b2222}
.cart-text{padding:3px 0 0 12px;font-size:11px;line-height:12px;color:#222}
.cart-text small{font-size:8px}
.search{left:558px;top:32px;width:176px;height:32px;background:#474747;padding:5px 4px;display:flex}
.search-field{flex:1;background:var(--white);font-size:8px;color:#aaa;font-style:italic;padding:6px}
.search-btn{width:24px;background:var(--green);display:flex;align-items:center;justify-content:center}
.nav{left:156px;top:64px;width:578px;height:33px;background:var(--nav);display:flex}
.nav a{font-family:"Roboto Condensed",sans-serif;font-size:12px;color:#d4d4d4;text-decoration:none;display:flex;align-items:center;justify-content:center;border-right:1px solid var(--nav-line);text-transform:uppercase}
.nav a.active{background:var(--green);color:var(--white)}
.nav a.strong{color:var(--white)}

/* hero */
.hero{left:0;top:99px;width:763px;height:331px;background:radial-gradient(ellipse at 28% 60%,#efe6de 0%,#c9b29f 28%,#8e6a55 60%,#5a4438 100%)}
.hero-title{left:356px;top:174px;font-family:"Roboto Condensed",sans-serif;font-size:40px;color:var(--white);letter-spacing:-.5px}
.hero-copy{left:358px;top:228px;width:330px;font-size:11.5px;line-height:17px;color:var(--white)}
.price-badge{left:607px;top:292px;width:79px;height:79px;border-radius:50%;background:#8a6c5c;border:3px solid #f0ebe6;box-shadow:0 2px 6px rgba(0,0,0,.4);text-align:center;color:var(--white)}
.price-badge .amt{font-family:"Roboto Condensed",sans-serif;font-style:italic;font-size:21px;margin-top:14px}
.price-badge .amt sup{font-size:10px;font-style:normal}
.price-badge .go{font-weight:700;font-size:12px;color:#f2e2a0;letter-spacing:.5px}

/* tiles */
.tile{top:454px;width:218px;height:125px}
.tile-shop{left:30px;background:linear-gradient(135deg,#8b7a6a,#5d4e45 60%,#9a4d4a)}
.tile-lamp{left:273px;background:linear-gradient(120deg,#6e5645,#c9b6a6 45%,#6b5140)}
.tile-figures{left:515px;background:linear-gradient(90deg,#c98c24,#e6a53a 50%,#6b4a1e)}
.shop-dot{left:112px;top:492px;width:52px;height:52px;border-radius:50%;background:var(--green);border:2px solid #2a7a30;color:var(--white);font-size:13px;font-weight:700;display:flex;align-items:center;justify-content:center}

/* latest product */
.section-line{left:30px;top:616px;width:704px;height:14px}
.section-title{left:0;width:763px;top:613px;text-align:center;font-family:"Roboto Condensed",sans-serif;font-size:16px;color:var(--green)}
.section-title span{background:var(--white);padding:0 6px}
.product-feature{left:30px;top:639px;width:165px;height:165px;background:var(--green);color:var(--white);text-align:center}
.product-feature .name{font-size:11px;margin-top:46px}
.product-feature .price{font-family:"Roboto Condensed",sans-serif;font-size:25px;margin-top:8px}
.product-card{top:639px;width:165px;height:165px;border:4px solid #d6d6d6}
.p1{left:210px;background:linear-gradient(120deg,#5d4535,#cdbcae 45%,#7b604c)}
.p2{left:390px;background:linear-gradient(160deg,#a98d6c,#6a5442 55%,#8e3f3a)}
.p3{left:569px;background:linear-gradient(160deg,#b88a4a,#5b3f24 55%,#8a6a45)}

/* news */
.news{left:30px;top:829px;width:704px;height:42px;background:var(--panel);display:flex;align-items:center}
.news-label{font-family:"Roboto Condensed",sans-serif;font-weight:300;font-size:21px;color:#888;width:65px;padding-left:10px;border-right:1px solid #c9c9c9;height:34px;line-height:34px}
.news-date{color:var(--green);font-size:9px;margin-left:10px}
.news-text{font-size:9px;color:#333;margin-left:7px}
.news-nav{left:694px;top:842px}

/* promos */
.promo{top:895px;height:86px}
.promo-chand{left:30px;width:166px;background:linear-gradient(135deg,#5b9e8a,#9cc6b6);color:var(--white)}
.promo-chand h3{font-family:"Roboto Condensed",sans-serif;font-weight:400;font-size:18px;margin:14px 0 0 5px}
.promo-chand p{font-size:8.5px;line-height:12px;margin:3px 0 0 6px;width:125px}
.promo-chand .cta{font-size:10px;font-weight:700;color:#222;margin:5px 0 0 7px}
.promo-lamps{left:204px;width:356px;background:#0e0e0e;color:var(--white);text-align:center}
.lamp-shade{left:26px;top:0;width:68px;height:86px;background:linear-gradient(90deg,#777,#eee 50%,#888)}
.lamp-red{left:290px;top:8px;width:50px;height:74px;background:linear-gradient(160deg,#c2231d,#444)}
.promo-lamps h3{font-family:"Roboto Condensed",sans-serif;font-weight:400;font-size:17px;color:var(--green);margin-top:12px}
.promo-lamps p{font-size:8.5px;line-height:13px;color:#ccc;margin-top:6px}
.promo-lamps .cta{font-size:10px;font-weight:700;margin-top:6px}
.promo-ship{left:566px;width:168px;background:var(--green);color:var(--white);padding:10px 0 0 14px}
.promo-ship .l1{font-family:"Roboto Condensed",sans-serif;font-weight:700;font-size:27px;letter-spacing:2px;line-height:28px}
.promo-ship .l2{font-family:"Roboto Condensed",sans-serif;font-weight:700;font-size:21px;letter-spacing:5px;line-height:24px}
.promo-ship .l3{font-size:10px;letter-spacing:1px;font-weight:700}

/* footer */
.footer{left:0;top:1005px;width:763px;height:154px;background:var(--footer)}
.col{top:1022px;font-family:"Open Sans",sans-serif;font-size:9px;color:#444}
.col h4{font-family:"Open Sans",sans-serif;font-weight:400;font-size:13px;line-height:16px;color:var(--green)}
.col-about{left:29px}
.col-about ul{margin-top:5px}
.col-about li{list-style:none;line-height:18.4px}
.col-news{left:216px;width:200px}
.col-news p{margin-top:8px;line-height:13.5px}
.subscribe{display:flex;margin-top:8px;height:23px}
.subscribe .field{width:127px;background:var(--white);font-size:8px;font-style:italic;color:#888;display:flex;align-items:center;gap:5px;padding-left:3px}
.subscribe .btn{width:70px;background:var(--green);color:var(--white);font-size:9px;font-style:italic;font-weight:600;display:flex;align-items:center;justify-content:center}
.socials{display:flex;gap:15px;margin-top:12px}
.socials i{width:17px;height:17px;border-radius:3px;background:#8a8a8a}
.socials i.s1{background:#3b5b98}
.col-contact{left:535px;width:200px}
.col-contact .lbl{font-style:italic;color:var(--green);font-size:10px}
.col-contact p{margin-top:10px;line-height:13.5px}
.divider{top:1015px;width:1px;height:142px;background:#c8c8c8}
.bottom{left:0;top:1159px;width:763px;height:41px;background:var(--bar)}
.copy{left:29px;top:1174px;font-family:"Open Sans",sans-serif;font-size:9px;color:#bbb}
.cards{left:550px;top:1170px;display:flex;gap:5px}
.cards i{width:26px;height:17px;border-radius:2px;background:#f1f1f1}
.cards i.c1{background:#6aa3d8}
</style>
</head>
<body>

<div class="abs header-rule"></div>
<div class="abs brand-box"><span class="brand-name">BRIGHTQUOKKA</span></div>

<div class="abs cart">
  <div class="cart-bag"></div>
  <div class="cart-text">Shopping Cart:<br><small>0 item(s) - $0.00</small></div>
</div>
<div class="abs search">
  <div class="search-field">Search</div>
  <div class="search-btn">
    <svg width="12" height="12" viewBox="0 0 12 12"><circle cx="7" cy="5" r="3.5" fill="none" stroke="#fff" stroke-width="1.5"/><line x1="4.5" y1="7.5" x2="1" y2="11" stroke="#fff" stroke-width="1.8"/></svg>
  </div>
</div>
<nav class="abs nav">
  <a class="active" style="width:50px">Home</a>
  <a style="width:73px">About Us</a>
  <a style="width:69px">Product</a>
  <a style="width:46px">Gift</a>
  <a style="width:80px">Light Bulb</a>
  <a style="width:84px">Contact Us</a>
  <a class="strong" style="width:85px">What's New</a>
  <a class="strong" style="width:91px;border-right:none">Shop by Brand</a>
</nav>

<div class="abs hero" role="img" aria-label="Photo of a white ceramic seal lamp in a blurred shop interior"></div>
<div class="abs hero-title">BRIGHT QUOKKA</div>
<p class="abs hero-copy">Lorem ipsum dolor sit amet, consectetur adipiscing elit. Nulla dictum arcu enim, a tempus sem sodales non.</p>
<div class="abs price-badge"><div class="amt"><sup>$</sup>50.00</div><div class="go">SHOP</div></div>

<div class="abs tile tile-shop" role="img" aria-label="Photo of a busy vintage shop floor"></div>
<div class="abs shop-dot">SHOP</div>
<div class="abs tile tile-lamp" role="img" aria-label="Photo of the seal lamp on a wooden table"></div>
<div class="abs tile tile-figures" role="img" aria-label="Photo of a row of cartoon cat telephones"></div>

<svg class="abs section-line" viewBox="0 0 704 14" width="704" height="14">
  <path d="M1 7 L8 2 M1 7 L8 12" stroke="#333" stroke-width="1.5" fill="none"/>
  <line x1="4" y1="7" x2="700" y2="7" stroke="#bbb" stroke-width="1"/>
  <line x1="4" y1="9" x2="700" y2="9" stroke="#ddd" stroke-width="1"/>
  <path d="M703 7 L696 2 M703 7 L696 12" stroke="#aaa" stroke-width="1.2" fill="none"/>
</svg>
<div class="abs section-title"><span>Latest Product</span></div>

<div class="abs product-feature">
  <div class="name">Lorem ipsum dolor</div>
  <div class="price">$50.00</div>
  <svg width="42" height="34" viewBox="0 0 42 34" style="margin-top:6px">
    <path d="M9 13 L19 4 L29 13" stroke="#fff" stroke-width="2.5" fill="none"/>
    <path d="M4 13 H36 L31 30 H11 Z" fill="#fff"/>
    <circle cx="31" cy="26" r="7" fill="#fff" stroke="#3fae49" stroke-width="2"/>
    <path d="M27.5 26 L30 28.5 L34.5 23.5" stroke="#3fae49" stroke-width="2" fill="none"/>
  </svg>
</div>
<div class="abs product-card p1" role="img" aria-label="Photo of the seal lamp"></div>
<div class="abs product-card p2" role="img" aria-label="Photo of a shop floor with radios and appliances"></div>
<div class="abs product-card p3" role="img" aria-label="Photo of hanging chandeliers in a shop"></div>

<div class="abs news">
  <div class="news-label">NEWS</div>
  <span class="news-date">04/02/2014</span>
  <span class="news-text">Lorem ipsum dolor sit amet, consectetur adipiscing elit. Nulla dictum arcu enim, a tempus sem sodales non.</span>
</div>
<svg class="abs news-nav" width="30" height="16" viewBox="0 0 30 16"><path d="M7 1 L2 8 L7 15" stroke="#777" stroke-width="1.8" fill="none"/><path d="M23 1 L28 8 L23 15" stroke="#3fae49" stroke-width="1.8" fill="none"/></svg>

<div class="abs promo promo-chand" role="img" aria-label="Chandelier promotion with a glowing lamp photo">
  <h3>Chandeliers</h3>
  <p>Lorem ipsum dolor sit amet, consectetur</p>
  <div class="cta">SHOP NOW</div>
</div>
<div class="abs promo promo-lamps">
  <div class="abs lamp-shade" role="img" aria-label="Photo of a silver floor lamp shade"></div>
  <div class="abs lamp-red" role="img" aria-label="Photo of a red desk lamp"></div>
  <h3>Floor lamps</h3>
  <p>Lorem ipsum dolor sit , consectetur<br>adipiscing elit. Nulla dictum arcu</p>
  <div class="cta">SHOP NOW</div>
</div>
<div class="abs promo promo-ship">
  <div class="l1">FREE
    <svg width="48" height="26" viewBox="0 0 48 26" style="vertical-align:-3px;margin-left:4px">
      <rect x="2" y="3" width="26" height="15" rx="3" fill="#1f1f1f"/>
      <path d="M29 7 H38 L44 13 V19 H29 Z" fill="#1f1f1f"/>
      <circle cx="10" cy="21" r="4" fill="#1f1f1f" stroke="#3fae49" stroke-width="1.5"/>
      <circle cx="37" cy="21" r="4" fill="#1f1f1f" stroke="#3fae49" stroke-width="1.5"/>
    </svg>
  </div>
  <div class="l2">SHIPPING</div>
  <div class="l3">ON ORDERS OVER $99.</div>
</div>

<div class="abs footer"></div>
<div class="abs divider" style="left:152px"></div>
<div class="abs divider" style="left:477px"></div>

<div class="abs col col-about">
  <h4>About Us</h4>
  <ul><li>Home</li><li>About Us</li><li>Product</li><li>Gift</li><li>Light Bulb</li><li>Contact us</li></ul>
</div>
<div class="abs col col-news">
  <h4>Subscribe to Our Newsletter</h4>
  <p>Lorem ipsum dolor sit amet, consr adipiscing elit. Aliquam</p>
  <div class="subscribe">
    <div class="field">
      <svg width="24" height="16" viewBox="0 0 24 16"><rect x="1" y="1" width="22" height="14" fill="none" stroke="#555" stroke-width="1.5"/><path d="M1 1 L12 9 L23 1" stroke="#555" stroke-width="1.5" fill="none"/></svg>
      your@email.com
    </div>
    <div class="btn">SUBSCRIBE</div>
  </div>
  <div class="socials"><i class="s1"></i><i></i><i></i><i></i><i></i><i></i></div>
</div>
<div class="abs col col-contact">
  <h4>Get In Touch</h4>
  <p style="margin-top:12px"><span class="lbl">Address:</span><br>Lorem ipsum dolor sit amet nec, consectetuer adipiscing elit. Aenemodo ligula</p>
  <p><span class="lbl">Phone:</span>&nbsp; +44 0161 555 019</p>
  <p><span class="lbl">Email:</span>&nbsp; info@brightquokka.net</p>
</div>

<div class="abs bottom"></div>
<div class="abs copy">© 2014 Brightquokka. All rights reserved.</div>
<div class="abs cards"><i class="c1"></i><i></i><i></i><i></i><i></i><i></i></div>

</body>
</html>
```